Business Card for Toffee Parlour

I have a logo for my candy buffet business, and need a business card designed using that logo. Toffee Parlour designs and builds beautiful and delicious candy and dessert tables for all kinds of events. The card should be simple, modern, graphic, colorful, and use the Toffee Parlour Logo.

Target Market(s)

The target market is people hosting major parties and events. This includes brides getting married, parents hosting birthday parties/Sweet Sixteen/Bar Mitzvah/quinceanera parties, and companies hosting corporate events.

Industry/Entity Type

Business

Requirements
Must have
• The business card must have the logo, with or without the tag line.

The following information must be on the card:

Renata Hollis
CEO & Candy Stylist
415.372.6091
renata@toffeeparlourco.example
Nice to have
• I like the idea of having multiple colors of the same design so that several people receiving cards will each receive a different color. Perhaps 3-5 colors or variations on a basic card design.

```html
<!DOCTYPE html>
<html lang="en">
<head>
<meta charset="utf-8">
<title>Toffee Parlour – Business Cards</title>
<link rel="stylesheet" href="https://fonts.googleapis.com/css2?family=Fira+Sans:wght@500;700;800&display=swap">
<style>
  :root {
    --canvas-bg: #e9e6e2;
    --card-white: #fbfaf8;
    --ink: #1c1c1c;
    --blue: #3a7fc1;
    --pink: #df1479;
    --yellow: #f1a93a;
    --green: #1f9a48;
    --purple: #6a4a9d;
    --card-w: 260px;
    --card-h: 150px;
  }
  * { box-sizing: border-box; margin: 0; padding: 0; }
  html, body { width: 1200px; height: 873px; overflow: hidden; }
  body {
    background: var(--canvas-bg);
    font-family: "Fira Sans", Arial, sans-serif;
    color: var(--ink);
  }
  .card-sheet {
    width: 1200px;
    height: 873px;
    display: flex;
    flex-direction: column;
    justify-content: center;
    align-items: center;
    gap: 50px;
  }
  .colour-row { display: flex; gap: 60px; }
  .card-pair { display: flex; gap: 20px; }

  .card {
    width: var(--card-w);
    height: var(--card-h);
    background: var(--card-white);
    position: relative;
    box-shadow: 0 2px 6px rgba(0,0,0,.15);
  }
  .accent-blue   { --accent: var(--blue); }
  .accent-pink   { --accent: var(--pink); }
  .accent-yellow { --accent: var(--yellow); }
  .accent-green  { --accent: var(--green); }
  .accent-purple { --accent: var(--purple); }

  /* Front: coloured frame with centred wordmark */
  .card-front {
    border: 12px solid var(--accent);
    display: flex;
    align-items: center;
    justify-content: center;
  }
  .wordmark {
    display: flex;
    align-items: center;
    gap: 8px;
  }
  .wordmark-dot {
    width: 14px;
    height: 14px;
    border-radius: 50%;
    background: var(--accent);
    flex: none;
  }
  .wordmark-name {
    font-weight: 500;
    font-size: 22px;
    letter-spacing: -0.3px;
    color: var(--ink);
  }

  /* Back: contact band */
  .card-back .wordmark {
    position: absolute;
    top: 12px;
    right: 14px;
    gap: 5px;
  }
  .card-back .wordmark-dot { width: 8px; height: 8px; }
  .card-back .wordmark-name { font-size: 11px; }

  .contact-band {
    position: absolute;
    left: 0;
    right: 0;
    top: 44px;
    height: 74px;
    background: var(--accent);
    color: #fff;
    display: flex;
    align-items: center;
    padding: 0 10px 0 14px;
  }
  .holder-name {
    font-weight: 800;
    font-size: 17px;
    line-height: 1.05;
    width: 78px;
  }
  .band-divider {
    width: 1.5px;
    height: 48px;
    background: #fff;
    margin: 0 9px 0 4px;
  }
  .contact-details {
    font-weight: 700;
    font-size: 8.4px;
    line-height: 1.45;
    white-space: nowrap;
  }
</style>
</head>
<body>
<main class="card-sheet">

  <div class="colour-row">
    <div class="card-pair accent-blue">
      <div class="card card-front">
        <div class="wordmark"><span class="wordmark-dot"></span><span class="wordmark-name">Toffee Parlour</span></div>
      </div>
      <div class="card card-back">
        <div class="wordmark"><span class="wordmark-dot"></span><span class="wordmark-name">Toffee Parlour</span></div>
        <div class="contact-band">
          <p class="holder-name">Renata<br>Hollis</p>
          <span class="band-divider"></span>
          <p class="contact-details">CEO &amp; Candy Stylist<br>415.372.6091<br>renata@toffeeparlourco.example</p>
        </div>
      </div>
    </div>

    <div class="card-pair accent-pink">
      <div class="card card-front">
        <div class="wordmark"><span class="wordmark-dot"></span><span class="wordmark-name">Toffee Parlour</span></div>
      </div>
      <div class="card card-back">
        <div class="wordmark"><span class="wordmark-dot"></span><span class="wordmark-name">Toffee Parlour</span></div>
        <div class="contact-band">
          <p class="holder-name">Renata<br>Hollis</p>
          <span class="band-divider"></span>
          <p class="contact-details">CEO &amp; Candy Stylist<br>415.372.6091<br>renata@toffeeparlourco.example</p>
        </div>
      </div>
    </div>
  </div>

  <div class="colour-row">
    <div class="card-pair accent-yellow">
      <div class="card card-front">
        <div class="wordmark"><span class="wordmark-dot"></span><span class="wordmark-name">Toffee Parlour</span></div>
      </div>
      <div class="card card-back">
        <div class="wordmark"><span class="wordmark-dot"></span><span class="wordmark-name">Toffee Parlour</span></div>
        <div class="contact-band">
          <p class="holder-name">Renata<br>Hollis</p>
          <span class="band-divider"></span>
          <p class="contact-details">CEO &amp; Candy Stylist<br>415.372.6091<br>renata@toffeeparlourco.example</p>
        </div>
      </div>
    </div>

    <div class="card-pair accent-green">
      <div class="card card-front">
        <div class="wordmark"><span class="wordmark-dot"></span><span class="wordmark-name">Toffee Parlour</span></div>
      </div>
      <div class="card card-back">
        <div class="wordmark"><span class="wordmark-dot"></span><span class="wordmark-name">Toffee Parlour</span></div>
        <div class="contact-band">
          <p class="holder-name">Renata<br>Hollis</p>
          <span class="band-divider"></span>
          <p class="contact-details">CEO &amp; Candy Stylist<br>415.372.6091<br>renata@toffeeparlourco.example</p>
        </div>
      </div>
    </div>
  </div>

  <div class="colour-row">
    <div class="card-pair accent-purple">
      <div class="card card-front">
        <div class="wordmark"><span class="wordmark-dot"></span><span class="wordmark-name">Toffee Parlour</span></div>
      </div>
      <div class="card card-back">
        <div class="wordmark"><span class="wordmark-dot"></span><span class="wordmark-name">Toffee Parlour</span></div>
        <div class="contact-band">
          <p class="holder-name">Renata<br>Hollis</p>
          <span class="band-divider"></span>
          <p class="contact-details">CEO &amp; Candy Stylist<br>415.372.6091<br>renata@toffeeparlourco.example</p>
        </div>
      </div>
    </div>
  </div>

</main>
</body>
</html>
```